KORVELTA Corporate Business Card

Modern business card design for company which focuses in the areas of Staffing, IT Consulting & Data Services. Please note: We are no longer using the IT subscript on the logo. All designs should have IT subscript removed.
Website: www.korveltait.example

```html
<!DOCTYPE html>
<html lang="en">
<head>
<meta charset="utf-8">
<title>KORVELTA Business Card</title>
<link href="https://fonts.googleapis.com/css2?family=Open+Sans:wght@400;700;800&display=swap" rel="stylesheet">
<style>
  :root {
    --brand-blue: #0a5a94;
    --accent-blue: #1b93d6;
    --logo-blue: #1f8fd4;
    --ink: #333333;
    --paper: #ffffff;
    --backdrop: #e9ebee;
  }
  * { box-sizing: border-box; margin: 0; padding: 0; }
  html, body {
    width: 1200px; height: 900px; overflow: hidden;
    background: var(--backdrop);
    font-family: "Open Sans", Arial, sans-serif;
  }
  .canvas { position: relative; width: 1200px; height: 900px; }
  .card {
    position: absolute; left: 250px; width: 700px; height: 400px;
    overflow: hidden;
    box-shadow: 0 6px 18px rgba(0,0,0,0.18);
  }
  .card--back { top: 40px; background: var(--brand-blue); }
  .card--front { top: 460px; background: var(--paper); }

  .wordmark {
    display: flex; align-items: center; gap: 10px;
    font-weight: 800; letter-spacing: 1px; line-height: 1;
  }
  .wordmark__square { width: 30px; height: 30px; border-radius: 5px; }
  .card--back .wordmark {
    position: absolute; left: 50%; top: 50%;
    transform: translate(-50%, -50%);
    color: var(--paper); font-size: 56px;
  }
  .card--back .wordmark__square { background: var(--paper); width: 40px; height: 40px; }

  .card--front .wordmark {
    position: absolute; left: 46px; top: 150px;
    color: var(--logo-blue); font-size: 44px;
  }
  .card--front .wordmark__square { background: var(--logo-blue); }

  .divider {
    position: absolute; left: 372px; top: 112px;
    width: 2px; height: 185px; background: var(--brand-blue);
  }
  .contact { position: absolute; left: 398px; top: 116px; color: var(--ink); }
  .contact__name {
    font-weight: 800; font-size: 27px; color: var(--brand-blue);
    letter-spacing: 0.5px; line-height: 1.05;
  }
  .contact__title { font-size: 18px; margin-bottom: 12px; }
  .contact__address { font-size: 19px; line-height: 1.3; margin-bottom: 10px; }
  .contact__line {
    display: flex; align-items: center; gap: 8px;
    font-size: 19px; line-height: 1.45;
  }
  .contact__line svg { width: 16px; height: 16px; fill: var(--accent-blue); flex: none; }

  .wave { position: absolute; left: 0; bottom: 0; width: 700px; height: 400px; }
  .website {
    position: absolute; right: 40px; bottom: 16px;
    color: var(--paper); font-size: 20px; letter-spacing: 0.5px; line-height: 1.2;
  }
</style>
</head>
<body>
<div class="canvas">
  <section class="card card--back" aria-label="Card back">
    <div class="wordmark"><span class="wordmark__square"></span>KORVELTA</div>
  </section>

  <section class="card card--front" aria-label="Card front">
    <svg class="wave" viewBox="0 0 700 400" aria-hidden="true">
      <path d="M0,262 C140,330 280,336 420,322 C540,310 640,306 700,330 L700,400 L0,400 Z" fill="var(--accent-blue)"/>
      <path d="M0,274 C140,342 280,348 420,334 C540,322 640,318 700,342" fill="none" stroke="var(--paper)" stroke-width="4"/>
      <path d="M0,282 C140,350 280,356 420,342 C540,330 640,326 700,350 L700,400 L0,400 Z" fill="var(--brand-blue)"/>
    </svg>

    <div class="wordmark"><span class="wordmark__square"></span>KORVELTA</div>
    <div class="divider"></div>

    <div class="contact">
      <p class="contact__name">DANA OSTRANDER</p>
      <p class="contact__title">President</p>
      <p class="contact__address">418 Harbor Lane<br>Riverton, IN 47000</p>
      <p class="contact__line">
        <svg viewBox="0 0 24 24"><path d="M6.6 10.8a15.2 15.2 0 0 0 6.6 6.6l2.2-2.2a1 1 0 0 1 1-.25 11.4 11.4 0 0 0 3.6.57 1 1 0 0 1 1 1V20a1 1 0 0 1-1 1A17 17 0 0 1 3 4a1 1 0 0 1 1-1h3.5a1 1 0 0 1 1 1c0 1.25.2 2.45.57 3.57a1 1 0 0 1-.25 1z"/></svg>
        555-014-2290
      </p>
      <p class="contact__line">
        <svg viewBox="0 0 24 24"><path d="M2 5h20v2l-10 6L2 7z M2 9l10 6 10-6v10H2z"/></svg>
        contactus@korveltait.example
      </p>
    </div>

    <p class="website">www.korveltait.example</p>
  </section>
</div>
</body>
</html>
```